Wirenexa

I'm looking to much improve our current website wirenexa.com
Updates

Low design quality

Target Market(s)

Commercial clients (Not-Residentials)

Industry/Entity Type

Office buildings and Industrial clients

Coding

Coded - Design and coding required

Number of Pages Required

5+ page

Requirements
Must have
• Very professional structured low voltage cabling projects for Wi-Fi, Audio/Video conference rooms, Access Control systems, CCTV.

```html
<!DOCTYPE html>
<html lang="en">
<head>
<meta charset="utf-8">
<title>Wirenexa — Structured Cabling for Commercial & Industrial</title>
<link href="https://fonts.googleapis.com/css2?family=Poppins:wght@400;500;600&family=Roboto:wght@500;700&display=swap" rel="stylesheet">
<style>
:root{
  --red:#d9302a;
  --red-dark:#c4261f;
  --ink:#161616;
  --muted:#6b6b6b;
  --light:#ececef;
  --line:#e2e2e6;
  --white:#fff;
  --footer:#1b1b1d;
  --hero-a:#0b2a55;
  --hero-b:#1c6fc2;
}
*{box-sizing:border-box;margin:0;padding:0}
html,body{width:1200px;height:5150px;overflow:hidden}
body{position:relative;font-family:"Poppins",sans-serif;color:var(--ink);background:var(--white)}
.abs{position:absolute}
h1,h2,h3,h4,.logo{font-family:"Roboto",sans-serif;font-weight:700}
.label{position:absolute;font-size:10px;letter-spacing:2px;color:var(--red);font-weight:600;text-transform:uppercase}
.h2{position:absolute;font-size:44px;line-height:50px;color:var(--ink)}
.btn{position:absolute;display:flex;align-items:center;background:var(--red);color:#fff;font-size:11px;font-weight:500;height:38px;padding-left:18px;border-radius:2px}
.btn .arrow{position:absolute;right:4px;top:4px;width:30px;height:30px;background:#fff;display:flex;align-items:center;justify-content:center}
.photo{position:absolute;border-radius:8px}

/* header */
.site-header{position:absolute;left:0;top:0;width:1200px;height:74px;background:#fff}
.logo{position:absolute;display:flex;align-items:center;gap:8px;font-size:28px}
.logo .mark{width:22px;height:22px;background:var(--red)}
.nav a{position:absolute;top:30px;font-size:11px;color:#555;text-decoration:none}
.nav a.active{color:var(--red)}
.nav a.active::after{content:"";position:absolute;left:4px;top:40px;width:16px;height:3px;background:var(--red)}
.phone-btn{position:absolute;left:888px;top:18px;width:152px;height:40px;background:var(--red);border-radius:3px;color:#fff;font-size:12px;font-weight:600;display:flex;align-items:center;padding-left:42px}
.phone-btn .ic{position:absolute;left:4px;top:4px;width:32px;height:32px;background:#fff;border-radius:2px;display:flex;align-items:center;justify-content:center}

/* hero */
.hero{position:absolute;left:0;top:74px;width:1200px;height:566px;background:linear-gradient(110deg,var(--hero-a) 0%,#13467f 40%,var(--hero-b) 75%,#3aa0e8 100%)}
.hero .kicker{position:absolute;left:160px;top:144px;color:#fff;font-size:18px;letter-spacing:3px;font-weight:500}
.hero h1{position:absolute;left:160px;top:170px;color:#fff;font-size:62px;line-height:66px}
.hero p{position:absolute;left:160px;top:324px;width:420px;color:#e6eefa;font-size:11px;line-height:20px}
.callback{position:absolute;left:766px;top:76px;width:274px;height:428px;border:2px solid rgba(255,255,255,.75);border-radius:10px;background:rgba(120,175,235,.35)}
.callback h3{position:absolute;top:18px;width:100%;text-align:center;color:#fff;font-size:20px;font-weight:500}
.callback .flabel{position:absolute;left:10px;font-size:8px;color:#fff}
.field{position:absolute;background:#fff;border-radius:3px;height:30px;display:flex;align-items:center;padding-left:10px;gap:10px;font-size:8px;color:#999}
.callback .field{left:10px;width:250px}
.check{position:absolute;display:flex;align-items:center;gap:10px;font-size:8px}
.check .box{width:16px;height:16px;background:#fff;border:1px solid #ccc;border-radius:2px}
.callback .submit{position:absolute;left:10px;top:360px;width:250px;height:38px;background:var(--red);color:#fff;font-size:11px;display:flex;align-items:center;justify-content:center;border-radius:2px}

/* about */
.about-title{left:634px;top:784px;font-size:42px;line-height:50px}
.about-title .accent{color:var(--red)}
.about-text{position:absolute;left:634px;top:998px;width:372px;font-size:11px;line-height:21px;color:var(--muted)}
.features-title{position:absolute;left:160px;top:1186px;font-size:24px}
.feature{position:absolute;top:1254px;width:160px}
.feature svg{display:block}
.feature h4{margin-top:20px;font-size:14px;line-height:20px;height:42px}
.feature p{margin-top:8px;font-size:9px;line-height:19px;color:var(--muted);height:76px}
.feature a{display:inline-block;margin-top:14px;font-size:10px;color:var(--red);text-decoration:underline}

/* services */
.services{position:absolute;left:0;top:1548px;width:1200px;height:640px;background:var(--light)}
.center{width:1200px;text-align:center;left:0}
.svc-card{position:absolute;top:242px;width:280px;height:322px;background:#fff;border-radius:4px}
.svc-card .img{position:absolute;left:12px;top:12px;width:256px;height:220px}
.svc-card .badge{position:absolute;left:28px;top:204px;width:62px;height:62px;border-radius:50%;background:var(--red);border:4px solid #fff;display:flex;align-items:center;justify-content:center}
.svc-card h4{position:absolute;left:24px;top:280px;font-size:18px;font-weight:500}

/* why */
.why-list{position:absolute;left:160px;top:2420px;list-style:none}
.why-list li{height:32px;font-size:12px;display:flex;align-items:center;gap:10px}
.why-list li::before{content:"»";color:var(--red);font-size:16px;font-weight:600}

/* stats */
.stats{position:absolute;left:0;top:2758px;width:1200px;height:258px;background:var(--red);color:#fff}
.stats h3{position:absolute;top:70px;width:100%;text-align:center;font-size:22px;font-weight:500}
.stat{position:absolute;top:128px}
.stat b{display:block;font-family:"Roboto",sans-serif;font-size:36px;font-weight:500}
.stat span{display:block;margin-top:4px;font-size:9px;letter-spacing:1.6px}

/* benefits */
.benefit{position:absolute;width:280px;border-left:0}
.benefit .icon{position:relative;height:52px;padding-left:14px;border-left:2px solid var(--red)}
.benefit h4{margin-top:22px;font-size:15px;font-weight:500}

/* testimonials */
.testimonials{position:absolute;left:0;top:3592px;width:1200px;height:574px;background:var(--light)}
.quote{position:absolute;top:190px;width:280px;height:228px;background:#fff;border-radius:4px}
.quote .stars{position:absolute;left:20px;top:26px;color:#f2b01e;font-size:13px;letter-spacing:1px}
.quote p{position:absolute;left:20px;top:50px;width:240px;font-size:11px;line-height:21px;color:#555}
.quote .avatar{position:absolute;left:18px;top:158px;width:50px;height:50px;border-radius:50%;background:linear-gradient(135deg,#b8a89a,#5c4a3e)}
.quote .who{position:absolute;left:76px;top:170px}
.quote .who b{display:block;font-family:"Roboto",sans-serif;font-size:13px;font-weight:500}
.quote .who span{display:block;font-size:8px;color:#888}
.circle-btn{position:absolute;top:454px;width:48px;height:48px;border-radius:50%;border:1.5px solid #444;display:flex;align-items:center;justify-content:center}

/* contact */
.c-label{position:absolute;font-size:10px;font-weight:500}
.contact .field{border:1px solid var(--line);height:36px}

/* footer */
.site-footer{position:absolute;left:0;top:4720px;width:1200px;height:430px;background:var(--footer);color:#fff}
.site-footer h4{position:absolute;top:72px;font-size:17px;font-weight:500}
.site-footer .links a{position:absolute;left:636px;font-size:11px;color:#ddd;text-decoration:none;letter-spacing:.5px}
.info{position:absolute;left:816px;display:flex;gap:14px}
.info .dot{width:28px;height:28px;border-radius:50%;border:1px solid #555;display:flex;align-items:center;justify-content:center}
.info small{display:block;font-size:7px;color:#999;letter-spacing:1px}
.info div.t{font-size:11px;line-height:20px}
.copy{position:absolute;left:160px;top:398px;font-size:10px;color:var(--red)}
.copy span{color:#fff}
</style>
</head>
<body>

<header class="site-header">
  <div class="logo" style="left:160px;top:20px"><span class="mark"></span>Wirenexa</div>
  <nav class="nav">
    <a class="active" href="#" style="left:620px">Home</a>
    <a href="#" style="left:676px">About Us</a>
    <a href="#" style="left:748px">Services</a>
    <a href="#" style="left:818px">Contact</a>
  </nav>
  <div class="phone-btn"><span class="ic"><svg width="16" height="16" viewBox="0 0 24 24" fill="none" stroke="#d9302a" stroke-width="2"><path d="M5 4h4l2 5-2.5 1.5a11 11 0 0 0 5 5L15 13l5 2v4a2 2 0 0 1-2 2A16 16 0 0 1 3 6a2 2 0 0 1 2-2"/></svg></span>(888)-555-0142</div>
</header>

<section class="hero" role="img" aria-label="Close-up of blue network cables plugged into a patch panel">
  <div class="kicker">Infrastructure That Keeps</div>
  <h1>Your Business<br>Connected</h1>
  <p>Structured cabling, fiber optics, network infrastructure, and technology solutions for commercial and industrial facilities.</p>
  <div class="btn" style="left:160px;top:388px;width:178px">Get a Project Quote<span class="arrow"><svg width="12" height="12" viewBox="0 0 12 12" stroke="#d9302a" stroke-width="1.4" fill="none"><path d="M3 9l6-6M4 3h5v5"/></svg></span></div>

  <form class="callback">
    <h3>Request Callback</h3>
    <span class="flabel" style="top:58px">Full Name *</span>
    <div class="field" style="top:74px"><svg width="14" height="14" viewBox="0 0 24 24" fill="none" stroke="#555" stroke-width="2"><circle cx="12" cy="12" r="10"/><circle cx="12" cy="10" r="3"/><path d="M6 19c2-3 10-3 12 0"/></svg>Type here . . .</div>
    <span class="flabel" style="top:116px">Phone *</span>
    <div class="field" style="top:132px"><svg width="14" height="14" viewBox="0 0 24 24" fill="none" stroke="#555" stroke-width="2"><path d="M5 4h4l2 5-2.5 1.5a11 11 0 0 0 5 5L15 13l5 2v4a2 2 0 0 1-2 2A16 16 0 0 1 3 6a2 2 0 0 1 2-2"/></svg>Type here . . .</div>
    <span class="flabel" style="top:174px">Email *</span>
    <div class="field" style="top:190px"><svg width="14" height="14" viewBox="0 0 24 24" fill="none" stroke="#555" stroke-width="2"><rect x="3" y="5" width="18" height="14"/><path d="M3 5l9 8 9-8"/></svg>Type here . . .</div>
    <span class="flabel" style="top:232px">Message *</span>
    <div class="field" style="top:248px;height:60px;align-items:flex-start;padding-top:10px"><svg width="14" height="14" viewBox="0 0 24 24" fill="none" stroke="#555" stroke-width="2"><path d="M4 4h16v12H8l-4 4z"/></svg>Type here . . .</div>
    <div class="check" style="left:10px;top:326px;color:#fff"><span class="box"></span>I'm not a robot</div>
    <div class="submit">Request Call</div>
  </form>
</section>

<div class="photo" role="img" aria-label="Ethernet cables in green and yellow connected to network switch" style="left:160px;top:716px;width:430px;height:416px;background:linear-gradient(135deg,#1d6e6a,#2a9a8a 40%,#c9c23a 75%,#486b2a)"></div>
<div class="label" style="left:634px;top:758px">About Us</div>
<h2 class="h2 about-title">Elevate Your<br>Connectivity with<br>Wire<span class="accent">nexa</span>'s<br>Cabling Solutions</h2>
<p class="about-text">Wirenexa is your premier provider of professional low voltage cabling services in Virginia, Washington DC, and Maryland. With a focus on quality, reliability, and attention to detail, we deliver exceptional cabling solutions for audio, video, security systems, computer networks, and more.</p>

<h3 class="features-title">Key Features of Our Cabling Services:</h3>
<div class="feature" style="left:160px">
  <svg width="40" height="40" viewBox="0 0 40 40" fill="none" stroke="#d9302a" stroke-width="1.6"><rect x="3" y="11" width="34" height="24" rx="2"/><path d="M14 11V6h12v5M3 21h34M18 21v4h4v-4"/></svg>
  <h4>Experience</h4>
  <p>With years of experience in the industry, our team brings a wealth of expertise to every cabling project.</p>
  <a href="#">Know More</a>
</div>
<div class="feature" style="left:335px">
  <svg width="40" height="40" viewBox="0 0 40 40" fill="none" stroke="#d9302a" stroke-width="1.6"><path d="M14 16a6 6 0 1 1 12 0c0 3-3 4-3 7h-6c0-3-3-4-3-7zM17 26h6M5 36l8-6h10M20 4V1M10 8 8 6M30 8l2-2"/></svg>
  <h4>Comprehensive Solutions</h4>
  <p>From copper CAT6 and CAT7 cabling to fiber optic installations (single and multimode) and Wi-Fi setup…</p>
  <a href="#">Know More</a>
</div>
<div class="feature" style="left:512px">
  <svg width="40" height="40" viewBox="0 0 40 40" fill="none" stroke="#d9302a" stroke-width="1.6"><circle cx="20" cy="20" r="16"/><circle cx="20" cy="20" r="11"/><path d="M15 20l4 4 7-8"/></svg>
  <h4>Quality Workmanship</h4>
  <p>At Wirenexa, we take pride in our work and strive for excellence in every project we undertake.</p>
  <a href="#">Know More</a>
</div>
<div class="feature" style="left:688px">
  <svg width="40" height="40" viewBox="0 0 40 40" fill="none" stroke="#d9302a" stroke-width="1.6"><path d="M3 37h34M6 37V12h14v25M20 37V18h14v19M10 17h3M10 23h3M10 29h3M24 23h3M24 29h3"/></svg>
  <h4>Commercial and Industrial</h4>
  <p>Whether you're a commercial business or an industrial facility, we have the expertise and resources to support…</p>
  <a href="#">Know More</a>
</div>
<div class="feature" style="left:864px">
  <svg width="40" height="40" viewBox="0 0 40 40" fill="none" stroke="#d9302a" stroke-width="1.6"><circle cx="20" cy="16" r="6"/><circle cx="8" cy="10" r="4"/><circle cx="32" cy="10" r="4"/><path d="M10 36c0-8 20-8 20 0M2 24c1-6 9-6 10-4M38 24c-1-6-9-6-10-4"/></svg>
  <h4>Customer Satisfaction</h4>
  <p>Our commitment to customer satisfaction drives everything we do. We work closely with our clients to understand their…</p>
  <a href="#">Know More</a>
</div>

<section class="services">
  <div class="label center" style="top:74px">Services</div>
  <h2 class="h2 center" style="top:94px">Complete Technology<br>Infrastructure Services</h2>
  <div class="svc-card" style="left:160px">
    <div class="img" role="img" aria-label="Technician working on network cables in a server rack" style="background:linear-gradient(135deg,#2f4b6e,#8ea4b8 50%,#d8dde2)"></div>
    <div class="badge"><svg width="24" height="24" viewBox="0 0 24 24" fill="none" stroke="#fff" stroke-width="1.6"><path d="M4 21V5h10v16M14 21V10h6v11M7 8h2M7 12h2M7 16h2"/></svg></div>
    <h4>Commercial Services</h4>
  </div>
  <div class="svc-card" style="left:460px">
    <div class="img" role="img" aria-label="Industrial plant with cooling towers at night" style="background:linear-gradient(180deg,#3a4250,#5a5f66 50%,#b0703a)"></div>
    <div class="badge"><svg width="24" height="24" viewBox="0 0 24 24" fill="none" stroke="#fff" stroke-width="1.6"><path d="M3 21V12l5 3v-3l5 3V6h3v15zM18 21V9h3v12"/></svg></div>
    <h4>Industrial Services</h4>
  </div>
  <div class="svc-card" style="left:760px">
    <div class="img" role="img" aria-label="Electrical panel with colourful wiring being tested" style="background:linear-gradient(135deg,#2f5f8a,#c7cfd6 55%,#d8b93a)"></div>
    <div class="badge"><svg width="24" height="24" viewBox="0 0 24 24" fill="none" stroke="#fff" stroke-width="1.6"><path d="M3 11l9-7 9 7M6 9v12h12V9M10 21v-6h4v6"/></svg></div>
    <h4>Residential Services</h4>
  </div>
</section>

<div class="label" style="left:160px;top:2274px">Why Choose Us</div>
<h2 class="h2" style="left:160px;top:2298px">Why Commercial<br>Clients Choose Us</h2>
<ul class="why-list">
  <li>Minimal disruption to operations</li>
  <li>Experienced project managers</li>
  <li>Safety-focused installation teams</li>
  <li>On-time project delivery</li>
  <li>Scalable infrastructure solutions</li>
  <li>Long-term support and maintenance</li>
</ul>
<div class="btn" style="left:160px;top:2614px;width:134px">Know More<span class="arrow"><svg width="12" height="12" viewBox="0 0 12 12" stroke="#d9302a" stroke-width="1.4" fill="none"><path d="M3 9l6-6M4 3h5v5"/></svg></span></div>
<div class="photo" role="img" aria-label="White patch cables plugged into a switch with glowing yellow port lights" style="left:608px;top:2262px;width:432px;height:420px;background:radial-gradient(circle at 45% 50%,#d9b23a,#6a5a36 45%,#2d2f33)"></div>

<section class="stats">
  <h3>Trusted By Businesses Across The Region</h3>
  <div class="stat" style="left:160px"><b>500+</b><span>PROJECTS COMPLETED</span></div>
  <div class="stat" style="left:384px"><b>25+</b><span>YEARS EXPERIENCE</span></div>
  <div class="stat" style="left:608px"><b>99.9%</b><span>NETWORK RELIABILITY</span></div>
  <div class="stat" style="left:834px"><b>100+</b><span>COMMERCIAL CLIENTS</span></div>
</section>

<div class="label" style="left:160px;top:3088px">Benefits</div>
<h2 class="h2" style="left:160px;top:3112px">Infrastructure Built for<br>Performance, Reliability,<br>and Growth</h2>

<div class="benefit" style="left:160px;top:3296px"><div class="icon"><svg width="40" height="44" viewBox="0 0 40 44" fill="none" stroke="#333" stroke-width="1.6"><rect x="6" y="4" width="10" height="16" rx="3"/><path d="M11 20v8a6 6 0 0 0 12 0V12a6 6 0 0 1 12 0v26"/></svg></div><h4>Voice & Data Cable Installations</h4></div>
<div class="benefit" style="left:460px;top:3296px"><div class="icon"><svg width="40" height="44" viewBox="0 0 40 44" fill="none" stroke="#333" stroke-width="1.6"><path d="M4 8l14 14 8 8M8 6l14 14M26 22h10M26 28h10M26 34h10"/></svg></div><h4>Copper Cable CAT6 and CAT7</h4></div>
<div class="benefit" style="left:760px;top:3296px"><div class="icon"><svg width="40" height="44" viewBox="0 0 40 44" fill="none" stroke="#333" stroke-width="1.6"><path d="M14 4v10M24 4v10M10 14h18v8H10zM19 22v20M12 30h14"/></svg></div><h4>Fiber Cable Single & Multi Mode</h4></div>
<div class="benefit" style="left:160px;top:3432px"><div class="icon"><svg width="40" height="44" viewBox="0 0 40 44" fill="none" stroke="#333" stroke-width="1.6"><ellipse cx="20" cy="22" rx="14" ry="10" transform="rotate(-40 20 22)"/><path d="M10 28l16-16M14 32l16-16M8 22l14-14"/></svg></div><h4>Conduit Installations</h4></div>
<div class="benefit" style="left:460px;top:3432px"><div class="icon"><svg width="40" height="44" viewBox="0 0 40 44" fill="none" stroke="#333" stroke-width="1.6"><rect x="10" y="4" width="16" height="22" rx="2"/><path d="M14 10h8M14 16h8M18 26v14"/></svg></div><h4>IDF and MDF Installations</h4></div>
<div class="benefit" style="left:760px;top:3432px"><div class="icon"><svg width="40" height="44" viewBox="0 0 40 44" fill="none" stroke="#333" stroke-width="1.6"><rect x="4" y="8" width="24" height="28" rx="2"/><path d="M9 14h14M9 20h14M9 26h8"/><circle cx="30" cy="28" r="6"/></svg></div><h4>Level 2G Tester Certification</h4></div>

<section class="testimonials">
  <div class="label center" style="top:74px">Testimonials</div>
  <h2 class="h2 center" style="top:98px">What Commercial Clients Say</h2>
  <div class="quote" style="left:160px"><div class="stars">★★★★★</div><p>"Wirenexa Group delivered our cabling project ahead of schedule with exceptional attention to detail."</p><div class="avatar" role="img" aria-label="Client portrait"></div><div class="who"><b>Marcus Hale</b><span>Facilities Director</span></div></div>
  <div class="quote" style="left:460px"><div class="stars">★★★★★</div><p>"Their team coordinated seamlessly with our construction schedule and exceeded expectations."</p><div class="avatar" role="img" aria-label="Client portrait"></div><div class="who"><b>Daniel Brooks</b><span>Operations Manager</span></div></div>
  <div class="quote" style="left:760px"><div class="stars">★★★★★</div><p>"Their team quickly understood our infrastructure requirements and delivered a solution that improved network performance across our entire facility."</p><div class="avatar" role="img" aria-label="Client portrait"></div><div class="who"><b>Laura Bennett</b><span>Director of Facilities & Operations</span></div></div>
  <div class="circle-btn" style="left:546px"><svg width="16" height="16" viewBox="0 0 16 16" fill="none" stroke="#333" stroke-width="1.5"><path d="M13 8H3M7 4 3 8l4 4"/></svg></div>
  <div class="circle-btn" style="left:606px"><svg width="16" height="16" viewBox="0 0 16 16" fill="none" stroke="#333" stroke-width="1.5"><path d="M3 8h10M9 4l4 4-4 4"/></svg></div>
</section>

<section class="contact">
  <div class="label" style="left:160px;top:4240px">Contact</div>
  <h2 class="h2" style="left:160px;top:4266px">Let's Discuss Your Next<br>Infrastructure Project</h2>
  <span class="c-label" style="left:160px;top:4398px">Full Name *</span>
  <span class="c-label" style="left:460px;top:4398px">Phone *</span>
  <span class="c-label" style="left:760px;top:4398px">Email *</span>
  <div class="field" style="left:160px;top:4420px;width:280px"><svg width="14" height="14" viewBox="0 0 24 24" fill="none" stroke="#555" stroke-width="2"><circle cx="12" cy="12" r="10"/><circle cx="12" cy="10" r="3"/><path d="M6 19c2-3 10-3 12 0"/></svg>Type here . . .</div>
  <div class="field" style="left:460px;top:4420px;width:280px"><svg width="14" height="14" viewBox="0 0 24 24" fill="none" stroke="#555" stroke-width="2"><path d="M5 4h4l2 5-2.5 1.5a11 11 0 0 0 5 5L15 13l5 2v4a2 2 0 0 1-2 2A16 16 0 0 1 3 6a2 2 0 0 1 2-2"/></svg>Type here . . .</div>
  <div class="field" style="left:760px;top:4420px;width:280px"><svg width="14" height="14" viewBox="0 0 24 24" fill="none" stroke="#555" stroke-width="2"><rect x="3" y="5" width="18" height="14"/><path d="M3 5l9 8 9-8"/></svg>Type here . . .</div>
  <span class="c-label" style="left:160px;top:4468px">Message *</span>
  <div class="field" style="left:160px;top:4490px;width:880px;height:60px;align-items:flex-start;padding-top:10px"><svg width="14" height="14" viewBox="0 0 24 24" fill="none" stroke="#555" stroke-width="2"><path d="M4 4h16v12H8l-4 4z"/></svg>Type here . . .</div>
  <div class="check" style="left:160px;top:4564px"><span class="box"></span>I'm not a robot</div>
  <div class="btn" style="left:160px;top:4606px;width:152px">Send Message<span class="arrow"><svg width="12" height="12" viewBox="0 0 12 12" stroke="#d9302a" stroke-width="1.4" fill="none"><path d="M3 9l6-6M4 3h5v5"/></svg></span></div>
</section>

<footer class="site-footer">
  <div class="logo" style="left:160px;top:64px;font-size:48px;color:#fff"><span class="mark" style="width:34px;height:34px"></span>Wirenexa</div>
  <h4 style="left:636px">Quick Links</h4>
  <div class="links">
    <a href="#" style="top:118px">»&nbsp; HOME</a>
    <a href="#" style="top:148px">»&nbsp; ABOUT US</a>
    <a href="#" style="top:178px">»&nbsp; SERVICES</a>
    <a href="#" style="top:208px">»&nbsp; CONTACT</a>
  </div>
  <h4 style="left:816px">Contact Us</h4>
  <div class="info" style="top:118px"><span class="dot"><svg width="12" height="12" viewBox="0 0 24 24" fill="none" stroke="#fff" stroke-width="2"><path d="M5 4h4l2 5-2.5 1.5a11 11 0 0 0 5 5L15 13l5 2v4a2 2 0 0 1-2 2A16 16 0 0 1 3 6a2 2 0 0 1 2-2"/></svg></span><div class="t"><small>PHONE</small><b>Local: 703-555-0187</b><br><b>National: (888) 555-0142</b></div></div>
  <div class="info" style="top:200px"><span class="dot"><svg width="12" height="12" viewBox="0 0 24 24" fill="none" stroke="#fff" stroke-width="2"><rect x="3" y="5" width="18" height="14"/><path d="M3 5l9 8 9-8"/></svg></span><div class="t"><small>EMAIL</small>sales@wirenexa.com</div></div>
  <div class="info" style="top:270px"><span class="dot"><svg width="12" height="12" viewBox="0 0 24 24" fill="none" stroke="#fff" stroke-width="2"><path d="M12 22s7-7 7-12a7 7 0 0 0-14 0c0 5 7 12 7 12z"/><circle cx="12" cy="10" r="2.5"/></svg></span><div class="t"><small>ADDRESS</small>4100 Lattice Ave, Suite 310<br>Fairview, VA 22000</div></div>
  <div class="copy">© 2026 All Rights Reserved | <span>Wirenexa</span></div>
</footer>

</body>
</html>
```